Business Card Design - Corporate

Create a sleek elegant business card layout while suggesting a color scheme. Convey cutting edge technology while maintaining a corporate feel that is easily readable.

Company designs and manufactures consumer electronic products for mass retail that are mainly app driven.

(vector logo and die-line provided)

Target Market(s)

Corporate level, tech industry.

Industry/Entity Type

Business

Contact Information for Business Card

Generic Info:

Name
Title
email
address
phone 1
phone 2
website (quelvane.com) on back

Font styles to use
Sans Serif

Requirements
Must have
• At least 2 colors + white on one side.
Nice to have
• Solid suggestion on color for logo and overall design. Color flood on back of card.
Should not have
• background texture like... marble, stone, patterns or circuit boards

```html
<!DOCTYPE html>
<html lang="en">
<head>
<meta charset="utf-8">
<title>Quelvane Business Card</title>
<link rel="stylesheet" href="https://fonts.googleapis.com/css2?family=Open+Sans:wght@400;600;700&display=swap">
<style>
  :root {
    --backdrop: #5b4838;
    --card-white: #ffffff;
    --card-grey: #5a5a5c;
    --ink: #4a4a4c;
    --ink-soft: #555557;
    --brand-blue: #1a76bb;
    --shadow: rgba(0, 0, 0, 0.35);
  }
  * { margin: 0; padding: 0; box-sizing: border-box; }
  html, body {
    width: 1200px;
    height: 987px;
    overflow: hidden;
    background: var(--backdrop);
    font-family: "Open Sans", sans-serif;
  }
  .card {
    position: absolute;
    left: 293px;
    width: 615px;
    height: 352px;
    border-radius: 19px;
    box-shadow: 0 3px 8px var(--shadow);
    overflow: hidden;
  }
  .card--front { top: 130px; background: var(--card-white); }
  .card--back  { top: 505px; background: var(--card-grey); }

  .wordmark {
    position: absolute;
    font-family: "Open Sans", sans-serif;
    font-weight: 400;
    font-size: 54px;
    letter-spacing: 6px;
    line-height: 1;
    white-space: nowrap;
  }
  .card--front .wordmark {
    right: 33px;
    top: 42px;
    color: var(--ink-soft);
  }
  .card--back .wordmark {
    left: 0;
    right: 0;
    top: 148px;
    text-align: center;
    color: var(--card-white);
    padding-left: 6px;
  }

  .person {
    position: absolute;
    left: 30px;
    top: 186px;
  }
  .person__name {
    font-size: 22px;
    font-weight: 700;
    color: var(--brand-blue);
    line-height: 1.2;
  }
  .person__title {
    font-size: 16.5px;
    color: var(--ink);
    line-height: 1.3;
  }
  .divider {
    position: absolute;
    left: 33px;
    right: 35px;
    top: 244px;
    height: 1.5px;
    background: var(--brand-blue);
  }
  .contact-list {
    position: absolute;
    left: 31px;
    top: 259px;
    list-style: none;
  }
  .contact-list li {
    display: flex;
    align-items: center;
    height: 23.5px;
    font-size: 16.5px;
    color: var(--ink);
  }
  .contact-list svg {
    width: 15px;
    height: 15px;
    margin-right: 8px;
    fill: var(--brand-blue);
    flex: none;
  }
  .address {
    position: absolute;
    right: 35px;
    top: 257px;
    text-align: right;
    font-style: normal;
    font-size: 16.5px;
    line-height: 23.5px;
    color: var(--ink);
  }
</style>
</head>
<body>
  <section class="card card--front">
    <div class="wordmark">QUELVANE</div>

    <div class="person">
      <div class="person__name">DANIEL REYES</div>
      <div class="person__title">CEO&amp;Founder</div>
    </div>

    <div class="divider"></div>

    <ul class="contact-list">
      <li>
        <svg viewBox="0 0 16 16" aria-hidden="true"><path d="M3.6 1.2 5.8 1l1.3 3.3-1.6 1.2c.8 1.9 2.1 3.3 4 4.1l1.3-1.5 3.2 1.4-.3 2.3c-.1.8-.8 1.3-1.6 1.3C6.5 12.9 2.5 8.6 2.3 2.8c0-.8.5-1.5 1.3-1.6z"/></svg>
        555 214 0387
      </li>
      <li>
        <svg viewBox="0 0 16 16" aria-hidden="true"><path d="M3.6 1.2 5.8 1l1.3 3.3-1.6 1.2c.8 1.9 2.1 3.3 4 4.1l1.3-1.5 3.2 1.4-.3 2.3c-.1.8-.8 1.3-1.6 1.3C6.5 12.9 2.5 8.6 2.3 2.8c0-.8.5-1.5 1.3-1.6z"/></svg>
        555 630 7219
      </li>
      <li>
        <svg viewBox="0 0 16 16" aria-hidden="true"><path d="M1 4h14v9H1z M1.8 4.6 8 9l6.2-4.4" stroke="#fff" stroke-width="1"/></svg>
        daniel@quelvane.com
      </li>
    </ul>

    <address class="address">
      2146 Willow Crest Drive<br>
      Harbor Falls, Alaska 99871<br>
      www.quelvane.com
    </address>
  </section>

  <section class="card card--back" role="img" aria-label="Grey card back with a faint repeating brand-mark pattern">
    <div class="wordmark">QUELVANE</div>
  </section>
</body>
</html>
```